Business Card Design Project

looking for a stylish and simple double sided business card.
I am an artist - specialising in fashion illustration, portraits and murals.
the front should be simply my name and tag:

D A V E R U
Living in colour

My preference is for a Black background with DAVERU in red or embossed.
Living in colour in White or multi-coloured.

the back will have detail:

Personalised Art
Portraits, Murals, Fashion Illustration

0487 312 560
daveru@daveru.com.au
www.daveru.com.au

Target Market(s)

Adults that are based in western speaking countries who have an appreciation for art and design. Portraits and wall art
Business owners who may need personalised all art for their business space. Murals and personalised canvass.
People in the fashion industry, who may require fashion illustrations.

Industry/Entity Type

Fashion

Requirements
Must have
• BOLD but simple at the same time, timeless modern element to it.
Nice to have
• simple lettering
Should not have
• Not too busy or wordy,

```html
<!DOCTYPE html>
<html lang="en">
<head>
<meta charset="utf-8">
<title>Daveru – Business Card</title>
<link rel="stylesheet" href="https://fonts.googleapis.com/css2?family=Jost:wght@300;400&display=swap">
<style>
  :root {
    --stage: #e6e6e4;
    --card-dark: #373f47;
    --card-light: #f4f4f4;
    --card-light-edge: #e4e4e4;
    --accent-red: #d9472b;
    --ink-light: #eef0f1;
    --ink-dark: #3b4249;
    --rule-dark: #4a5158;
  }
  * { margin: 0; padding: 0; box-sizing: border-box; }
  html, body {
    width: 1200px;
    height: 1000px;
    overflow: hidden;
    background: var(--stage);
    font-family: "Jost", "Helvetica Neue", Arial, sans-serif;
  }
  .canvas {
    position: relative;
    width: 1200px;
    height: 1000px;
  }
  .card {
    position: absolute;
    border-radius: 22px;
  }

  /* Front */
  .card-front {
    left: 160px;
    top: 160px;
    width: 660px;
    height: 420px;
    background: var(--card-dark);
  }
  .brand-name {
    position: absolute;
    left: 0;
    right: 0;
    top: 165px;
    text-align: center;
    color: var(--accent-red);
    font-weight: 300;
    font-size: 50px;
    letter-spacing: 0.2em;
    padding-left: 0.2em;
    line-height: 1;
  }
  .brand-tagline {
    position: absolute;
    left: 0;
    right: 0;
    top: 245px;
    text-align: center;
    color: var(--ink-light);
    font-weight: 300;
    font-size: 26px;
    letter-spacing: 0.2em;
    padding-left: 0.2em;
    line-height: 1;
  }

  /* Back */
  .card-back {
    left: 405px;
    top: 488px;
    width: 640px;
    height: 370px;
    background: radial-gradient(ellipse at 50% 55%, #ffffff 0%, var(--card-light) 55%, var(--card-light-edge) 100%);
    box-shadow: 0 2px 6px rgba(0, 0, 0, 0.18);
  }
  .offer-title {
    position: absolute;
    left: 0;
    right: 0;
    top: 80px;
    text-align: center;
    color: var(--accent-red);
    font-weight: 400;
    font-size: 25px;
    letter-spacing: 0.5em;
    padding-left: 0.5em;
    line-height: 1;
  }
  .offer-rule {
    position: absolute;
    left: 47px;
    right: 40px;
    top: 124px;
    height: 1px;
    background: var(--rule-dark);
  }
  .offer-services {
    position: absolute;
    left: 0;
    right: 0;
    top: 134px;
    text-align: center;
    color: var(--ink-dark);
    font-weight: 400;
    font-size: 20px;
    letter-spacing: 0.17em;
    padding-left: 0.17em;
    line-height: 1;
  }
  .contact-list {
    position: absolute;
    left: 0;
    right: 0;
    top: 204px;
    list-style: none;
    text-align: center;
    color: var(--ink-dark);
    font-weight: 400;
    font-size: 19px;
    letter-spacing: 0.18em;
    padding-left: 0.18em;
  }
  .contact-list li { line-height: 33px; }
</style>
</head>
<body>
  <main class="canvas">
    <section class="card card-front" aria-label="Business card front">
      <h1 class="brand-name">DAVERU</h1>
      <p class="brand-tagline">LIVING IN COLOUR</p>
    </section>

    <section class="card card-back" aria-label="Business card back">
      <h2 class="offer-title">PERSONALISED ART</h2>
      <div class="offer-rule"></div>
      <p class="offer-services">PORTRAITS | MURALS | FASHION ILLUSTRATION</p>
      <ul class="contact-list">
        <li class="contact-phone">0487 312 560</li>
        <li class="contact-email">daveru@daveru.com.au</li>
        <li class="contact-web">www.daveru.com.au</li>
      </ul>
    </section>
  </main>
</body>
</html>
```